Creative 1 page website design with html coding needed to go with Game Pre-Registration App

Velvet Arcade Club
~Discover games before release~

Website keywords: Simple, slick, stylish
Colors: Black, white, pink (like our logo)

***draft can be created in PSD or HTML***

We have a brand new service called Velvet Arcade Club which will be a game app pre-registration service. We already have the icon & UI for the app and we are looking for a slick & stylish corporate website to go with the service.

This will be a corporate website aim for businesses to contact us. Consumers will not be able to pre-register for games here. We do however want consumers to download our app from Zorvik Shelf after landing here.

Some framework we have in mind for 1 page website:
Home - default page showing the UI of the app and Zorvik Shelf icon with store link.
Our Service - quick explanation about our service & it's strength
Clients - logos of our clients
Press-
Pricing - basic usage is free. There will be premium services customers can use on a performance basis (CPA).
Contact Us

Call to action will be 1. Download the app 2. Contact us

We would like to be able to edit the press and clients section with web developer's support.

website in image:
https://www.marlowbyte.com/

Target Market(s)

Marketing managers of game developer. We want game developers to find out about our service and get in touch with us. The service will only be available in USA.

Midcore gamers in USA: Our end users will be game enthusiasts from US. Male aged 15-35.

Industry/Entity Type

Games

Font styles to use
Sans Serif

Colors
000000
ffffff
e567a6
e34097

Requirements
Must have
• - Only use our colors from the logo attached.
- UI of our app with an Quilbo phone
- Link to Zorvik Shelf Store
- slick & modern design
- Font used: Century Gothic

```html
<!DOCTYPE html>
<html lang="en">
<head>
<meta charset="utf-8">
<title>Velvet Arcade Club</title>
<link href="https://fonts.googleapis.com/css2?family=Poppins:wght@300;400;600;700&display=swap" rel="stylesheet">
<style>
:root{
  --black:#000000;
  --ink:#1d1d1f;
  --dark:#2a2a2c;
  --white:#ffffff;
  --pink:#e34097;
  --pink-soft:#e567a6;
  --grey:#8a8a8a;
  --grey-light:#f1f1f1;
  --line:#d6d6d6;
}
*{margin:0;padding:0;box-sizing:border-box}
html,body{width:1200px;height:4472px;overflow:hidden}
body{font-family:"Poppins",sans-serif;color:var(--ink);background:var(--white);position:relative}
section,header,footer{position:absolute;left:0;width:1200px;overflow:hidden}
.abs{position:absolute}
.pink{color:var(--pink)}
.section-title{position:absolute;left:0;width:1200px;text-align:center;font-size:30px;color:#7a7a7a;font-weight:600}
.section-title::after{content:"";display:block;width:60px;height:4px;background:var(--pink);margin:22px auto 0}

/* hero */
.hero{top:0;height:745px;background:radial-gradient(ellipse at 78% 45%,#4a1033 0%,#1a0b16 40%,#0c0c0e 75%)}
.brand{position:absolute;display:flex;align-items:center;gap:14px;color:var(--white);font-size:30px;font-weight:700}
.brand .mark{width:36px;height:36px;background:var(--pink);border-radius:6px}
.nav{position:absolute;top:40px;right:45px;display:flex;gap:50px;font-size:24px;color:var(--white)}
.nav .active{color:var(--pink);border-bottom:4px solid var(--pink);padding-bottom:10px}
.hero h1{position:absolute;left:45px;top:240px;font-size:46px;line-height:1.25;color:var(--white);font-weight:700}
.hero h1 span{color:var(--pink)}
.hero .lead{position:absolute;left:45px;top:420px;width:430px;font-size:21px;line-height:1.4;color:#e8e8e8}
.store-btn{position:absolute;top:555px;height:72px;border:2px solid #888;border-radius:10px;background:#000;color:var(--white);padding:10px 22px;font-size:14px;line-height:1.2}
.store-btn b{display:block;font-size:25px;font-weight:600}

/* why */
.why{top:745px;height:615px;background:var(--white)}
.feature{position:absolute;top:175px;width:360px;text-align:center}
.feature .icon{width:190px;height:190px;border-radius:50%;margin:0 auto;background:#e6e6e6;display:flex;align-items:center;justify-content:center}
.feature.on .icon{background:var(--pink)}
.feature h3{margin-top:42px;font-size:24px;font-weight:700}
.feature.on h3{color:var(--pink)}
.feature p{margin-top:8px;font-size:18px;color:var(--grey);line-height:1.35}

/* facts */
.facts{top:1360px;height:708px;background:var(--grey-light)}
.facts .label{position:absolute;left:480px;top:60px;font-size:28px;color:#7a7a7a;font-weight:600}
.facts .label::after{content:"";display:block;width:60px;height:4px;background:var(--pink);margin:18px auto 0}
.reach{position:absolute;left:615px;top:185px;width:540px;text-align:right}
.reach h2{font-size:34px;font-weight:600;border-bottom:2px solid #c9c9c9;padding-bottom:20px}
.reach p{margin-top:20px;font-size:25px;color:#777;line-height:1.3}
.donut{position:absolute;top:395px;width:250px;height:250px}
.donut .txt{position:absolute;inset:0;display:flex;flex-direction:column;align-items:center;justify-content:center;font-size:28px;color:#555}
.donut .txt b{font-size:46px;font-weight:400;color:var(--pink)}

/* slider */
.slider{top:2068px;height:262px;background:linear-gradient(#dcdcdc,#c4c4c4)}
.slide{position:absolute;top:0;height:262px;width:393px;background:linear-gradient(180deg,#e6e6e6,#bdbdbd);border-right:6px solid #f4f4f4}
.slider h2{position:absolute;left:0;width:1200px;top:80px;text-align:center;font-size:46px;font-weight:400;color:#222}
.arrow{position:absolute;width:56px;height:56px;border-radius:50%;display:flex;align-items:center;justify-content:center}

/* testimonial */
.testimonial{top:2330px;height:410px;background:var(--pink)}
.testimonial .quote{position:absolute;left:253px;top:50px;width:500px;font-size:25px;line-height:1.32;color:var(--white)}
.testimonial .who{position:absolute;left:253px;top:268px;font-size:15px;color:#fbd5e8;font-style:italic}
.partner{position:absolute;left:800px;top:0;width:400px;height:410px;background:var(--dark);display:flex;align-items:center;justify-content:center;gap:18px;color:var(--white);font-size:48px;font-weight:700}
.partner .mark{width:56px;height:56px;border-radius:50%;background:var(--pink-soft)}

/* clients */
.clients{top:2740px;height:205px;background:var(--white)}
.client{position:absolute;top:88px;width:220px;text-align:center;font-size:26px;font-weight:600;color:#777}

/* news */
.news{top:2945px;height:938px;background:var(--white)}
.card{position:absolute;top:205px;width:328px}
.card .pic{height:223px;position:relative}
.card .date{position:absolute;left:40px;top:18px;width:74px;height:74px;border-radius:50%;background:var(--pink);color:var(--white);text-align:center;font-size:15px;line-height:1.1;padding-top:16px;font-weight:600}
.card .date b{display:block;font-size:24px}
.card h3{margin-top:34px;font-size:27px;line-height:1.3;font-weight:700}
.card p{margin-top:18px;font-size:15px;line-height:1.45;color:#666}
.card .rule{margin:34px auto 0;width:110px;height:4px;background:#cfcfcf}
.dots{position:absolute;display:flex;gap:18px}
.dots i{width:22px;height:22px;border-radius:50%;background:#cfcfcf;display:block}
.dots i.on{background:var(--pink)}

/* contact */
.contact{top:3883px;height:291px;background:linear-gradient(180deg,#3b3b3d,#1f1f21)}
.contact h2{position:absolute;left:0;width:1200px;top:52px;text-align:center;font-size:68px;font-weight:700;color:var(--white)}
.contact p{position:absolute;left:0;width:1200px;top:150px;text-align:center;font-size:19px;color:#ddd}
.contact .btn{position:absolute;left:485px;top:200px;width:230px;height:62px;border:2px solid #555;background:#141414;color:var(--pink);font-size:21px;display:flex;align-items:center;justify-content:center}

.social{top:4174px;height:93px;background:var(--pink);display:flex}
.social span{flex:1;display:flex;align-items:center;justify-content:center;color:var(--white);font-size:24px;font-weight:600;border-right:2px solid rgba(255,255,255,.35)}
.social span:last-child{border-right:0}

.site-footer{top:4267px;height:173px;background:var(--white)}
.site-footer .brand{left:0;width:1200px;justify-content:center;top:28px;font-size:24px;color:#999}
.site-footer .brand .mark{width:28px;height:28px;background:#bbb}
.footer-nav{position:absolute;top:98px;left:0;width:1200px;display:flex;justify-content:center;gap:78px;font-size:24px;color:#999}
.footer-nav .active{color:var(--pink);border-bottom:3px solid var(--pink);padding-bottom:6px}
.legal{top:4440px;height:32px;background:var(--black);color:#ccc;font-size:14px;text-align:center;line-height:32px}
</style>
</head>
<body>

<header class="hero">
  <div class="brand" style="left:45px;top:36px"><span class="mark"></span>Velvet Arcade Club</div>
  <nav class="nav"><span class="active">Home</span><span>Our Service</span><span>Clients</span><span>Press</span><span>Contact Us</span></nav>
  <h1>Reach The Highly<br>Engaged <span>Audience</span></h1>
  <p class="lead">Lorem ipsum dolor sit amet, consectetuer elit, sed diam tincidunt.</p>
  <a class="store-btn" style="left:45px;width:215px">GET IT ON<b>Zorvik Shelf</b></a>
  <a class="store-btn" style="left:300px;width:210px">AVAILABLE ON<b>Quilbo</b></a>
  <svg class="abs" style="left:0;top:0" width="1200" height="745" aria-hidden="true">
    <path d="M660 560 C 760 380, 1080 300, 1180 120" stroke="#e34097" stroke-width="4" fill="none" opacity=".7"/>
    <path d="M640 640 C 800 470, 1100 420, 1200 260" stroke="#e567a6" stroke-width="2" fill="none" opacity=".5"/>
    <rect x="912" y="300" width="244" height="480" rx="34" fill="#2b2b2e" stroke="#777" stroke-width="3"/>
    <rect x="928" y="360" width="212" height="400" fill="#3a2a36"/>
    <rect x="708" y="225" width="262" height="560" rx="38" fill="#e9e9ea" stroke="#9a9a9a" stroke-width="3"/>
    <rect x="726" y="300" width="226" height="460" fill="#222"/>
    <path d="M580 660 l20 18 l20 -18" stroke="#fff" stroke-width="5" fill="none"/>
  </svg>
  <div class="abs" role="img" aria-label="App home screen listing upcoming games" style="left:726px;top:300px;width:226px;height:445px;background:linear-gradient(180deg,#ffffff 0 14%,#f2f2f2 14% 100%)"></div>
  <div class="abs" role="img" aria-label="Game artwork thumbnails in the app list" style="left:736px;top:380px;width:80px;height:360px;background:linear-gradient(180deg,#8a5a3a,#3f7aa8 50%,#b44a3a)"></div>
</header>

<section class="why">
  <h2 class="section-title" style="top:50px">Why Should You Chose Us!</h2>
  <div class="feature on" style="left:36px">
    <div class="icon"><svg width="90" height="90" viewBox="0 0 90 90" aria-hidden="true"><rect x="16" y="8" width="50" height="70" rx="5" fill="none" stroke="#fff" stroke-width="5"/><rect x="44" y="30" width="30" height="48" rx="4" fill="#e34097" stroke="#fff" stroke-width="5"/></svg></div>
    <h3>100% Cross-Platform</h3><p>Lorem ipsum dolor sit amet,<br>consectetuer adipiscing elit</p>
  </div>
  <div class="feature" style="left:416px">
    <div class="icon"><svg width="90" height="90" viewBox="0 0 90 90" aria-hidden="true"><rect x="10" y="14" width="70" height="56" rx="6" fill="none" stroke="#9c9c9c" stroke-width="5"/><line x1="10" y1="28" x2="80" y2="28" stroke="#9c9c9c" stroke-width="5"/><circle cx="45" cy="48" r="10" fill="#9c9c9c"/></svg></div>
    <h3>High Quality Games</h3><p>Lorem ipsum dolor sit amet,<br>consectetuer adipiscing elit</p>
  </div>
  <div class="feature" style="left:808px">
    <div class="icon"><svg width="100" height="90" viewBox="0 0 100 90" aria-hidden="true"><path d="M12 70 A38 38 0 0 1 88 70" fill="none" stroke="#9c9c9c" stroke-width="7"/><line x1="50" y1="70" x2="70" y2="40" stroke="#9c9c9c" stroke-width="6"/><circle cx="50" cy="70" r="7" fill="#9c9c9c"/></svg></div>
    <h3>Flawless Performance</h3><p>Lorem ipsum dolor sit amet, con-<br>sectetuer adipiscing elit</p>
  </div>
</section>

<section class="facts">
  <svg class="abs" style="left:90px;top:38px" width="320" height="680" aria-hidden="true">
    <rect x="3" y="3" width="314" height="680" rx="40" fill="#e9e9ea" stroke="#888" stroke-width="3"/>
    <rect x="22" y="70" width="276" height="610" fill="#fafafa"/>
  </svg>
  <svg class="abs" style="left:165px;top:295px" width="340" height="340" aria-hidden="true">
    <circle cx="170" cy="170" r="165" fill="#222" stroke="#fff" stroke-width="8"/>
  </svg>
  <div class="abs" role="img" aria-label="Magnified app news screen with game artwork" style="left:210px;top:370px;width:250px;height:210px;border-radius:20px;background:linear-gradient(135deg,#2f6a8c,#6a9a3a 55%,#c28a2a)"></div>
  <h2 class="label">Facts &amp; Figures</h2>
  <div class="reach"><h2>Reach: Over 700 Million People</h2><p>Lorem ipsum dolor sit amet,<br>onsectetuer sed diam nonummy</p></div>
  <div class="donut" style="left:639px">
    <svg width="250" height="250" aria-hidden="true"><circle cx="125" cy="125" r="110" fill="#fff" stroke="#d8d8d8" stroke-width="14"/><circle cx="125" cy="125" r="110" fill="none" stroke="#e34097" stroke-width="14" stroke-dasharray="318 691" transform="rotate(-90 125 125)"/></svg>
    <div class="txt"><b>46%</b>Female<br>Gamers</div>
  </div>
  <div class="donut" style="left:881px">
    <svg width="250" height="250" aria-hidden="true"><circle cx="125" cy="125" r="110" fill="#fff" stroke="#d8d8d8" stroke-width="14"/><circle cx="125" cy="125" r="110" fill="none" stroke="#e34097" stroke-width="14" stroke-dasharray="401 691" transform="rotate(-90 125 125)"/></svg>
    <div class="txt"><b>58%</b>Male<br>Gamers</div>
  </div>
</section>

<section class="slider">
  <div class="slide" style="left:0"></div><div class="slide" style="left:400px"></div><div class="slide" style="left:800px"></div>
  <h2>Recent Game screen goes here</h2>
  <div class="arrow" style="left:39px;top:82px;background:#555"><svg width="20" height="20" aria-hidden="true"><path d="M13 3 L6 10 L13 17" stroke="#fff" stroke-width="3" fill="none"/></svg></div>
  <div class="arrow" style="left:1109px;top:82px;background:var(--pink)"><svg width="20" height="20" aria-hidden="true"><path d="M7 3 L14 10 L7 17" stroke="#fff" stroke-width="3" fill="none"/></svg></div>
</section>

<section class="testimonial">
  <div class="abs" style="left:232px;top:20px;font-size:140px;line-height:1;color:var(--pink-soft);font-weight:700">“</div>
  <div class="abs" role="img" aria-label="Portrait of the content manager" style="left:55px;top:73px;width:150px;height:150px;border-radius:50%;border:6px solid #fff;background:linear-gradient(180deg,#c9a48a,#6a6f7a)"></div>
  <p class="quote">Lorem ipsum dolor sit amet, consectetuer adipiscing elit, sed diam nonummy nibh euismod tincidunt ut laoreet dolore magna aliquam erat volutpat.</p>
  <p class="who">Tomas Reyl Content Manager</p>
  <div class="dots" style="left:262px;top:320px;gap:10px"><i style="width:16px;height:16px;background:#333"></i><i style="width:16px;height:16px;background:#b02a74"></i><i style="width:16px;height:16px;background:#b02a74"></i><i style="width:16px;height:16px;background:#b02a74"></i><i style="width:16px;height:16px;background:#b02a74"></i></div>
  <svg class="abs" style="left:690px;top:315px" width="80" height="30" aria-hidden="true"><rect width="36" height="30" fill="#b02a74"/><rect x="42" width="36" height="30" fill="#b02a74"/><path d="M22 8 L14 15 L22 22" stroke="#fff" stroke-width="3" fill="none"/><path d="M56 8 L64 15 L56 22" stroke="#fff" stroke-width="3" fill="none"/></svg>
  <div class="partner"><span class="mark"></span>Norvane</div>
</section>

<section class="clients">
  <span class="client" style="left:20px">Odessa Print</span>
  <span class="client" style="left:235px">Brakka</span>
  <span class="client" style="left:450px;color:#333">Norvane</span>
  <span class="client" style="left:705px">Keystrand</span>
  <span class="client" style="left:960px">Orvy Nutritional</span>
</section>

<section class="news">
  <h2 class="section-title" style="top:50px">News &amp; Event</h2>
  <article class="card" style="left:45px">
    <div class="pic" role="img" aria-label="Illustration of marketing and social media icons" style="background:linear-gradient(135deg,#7fd0e0,#3fa7c4)"><div class="date">SEP<b>25</b></div></div>
    <h3>Lorem ipsum dolor sit amet lorem</h3>
    <p>Typi non habent claritatem insitam; est usus legentis in iis qui facit eorum claritatem. Investigationes demonstraverunt lectores legere me lius quod ii legunt saepius.</p>
    <div class="rule"></div>
  </article>
  <article class="card" style="left:436px">
    <div class="pic" role="img" aria-label="Illustration of a laptop surrounded by app icons" style="background:linear-gradient(135deg,#f4f4f4,#d8d8d8)"><div class="date">SEP<b>24</b></div></div>
    <h3>Lorem ipsum dolor sit amet lorem</h3>
    <p>Typi non habent claritatem insitam; est usus legentis in iis qui facit eorum claritatem. Investigationes demonstraverunt lectores legere me lius quod ii legunt saepius.</p>
    <div class="rule"></div>
  </article>
  <article class="card" style="left:827px">
    <div class="pic" role="img" aria-label="Illustration of charts and business graphics" style="background:linear-gradient(135deg,#e8eef2,#9ec6d6)"><div class="date">SEP<b>23</b></div></div>
    <h3>Lorem ipsum dolor sit amet lorem</h3>
    <p>Typi non habent claritatem insitam; est usus legentis in iis qui facit eorum claritatem. Claritas est etiam processus dynamicus, qui sequitur mutationem.</p>
    <div class="rule"></div>
  </article>
  <div class="dots" style="left:527px;top:870px"><i class="on"></i><i></i><i></i></div>
</section>

<section class="contact" role="img" aria-label="Team working together in an office, darkened background">
  <h2>Get in Touch</h2>
  <p>We're growing...fast! Become a part in our exciting journey and join our talented global team.</p>
  <span class="btn">Join with us</span>
</section>

<section class="social"><span>Facelane</span><span>Chirply</span><span>Plusgrid</span><span>Netlinkr</span></section>

<footer class="site-footer">
  <div class="brand"><span class="mark"></span>Velvet Arcade Club</div>
  <nav class="footer-nav"><span class="active">Home</span><span>Our Service</span><span>Clients</span><span>Press</span><span>Contact Us</span></nav>
</footer>
<section class="legal">© 2014 Velvet Arcade Club, Inc. &nbsp;|&nbsp; Security &nbsp;|&nbsp; Privacy Policy &nbsp;|&nbsp; Terms of Use</section>

</body>
</html>
```